Powerpoint design for european B2B business

We need a Powerpoint design for a newly established IT company with a B2B focus. We want to develop management information systems that help managers communicate goals into their organization and analyze their organizational activities and performance.

We defined the attached color scale, please relate your design to these colors.

The design should be simple and straight, serious and professional and leave enough space for the content ... :-)

Target Market(s)

B2B, companies larger than 200 employees

Industry/Entity Type

Business

Font styles to use
Sans Serif

Requirements
Should not have
• too playful design, clipart style

```html
<!DOCTYPE html>
<html lang="en">
<head>
<meta charset="utf-8">
<title>Presentation Template – Slide Layouts</title>
<link href="https://fonts.googleapis.com/css2?family=Open+Sans:wght@300;400;700&display=swap" rel="stylesheet">
<style>
:root{
  --navy:#264a6e;
  --red:#c43b52;
  --yellow:#e3dd55;
  --green:#8cc09b;
  --body:#555a60;
  --muted:#8a8d90;
  --rule:#e4e6e8;
  --frame:#9a9a9a;
  --bg:#ffffff;
}
*{margin:0;padding:0;box-sizing:border-box}
html,body{width:1200px;height:1200px;overflow:hidden;background:var(--bg)}
body{font-family:"Open Sans",Arial,sans-serif;position:relative}
.slide{position:absolute;width:547px;height:308px;background:#fff;border:1px solid var(--frame);box-shadow:0 1px 3px rgba(0,0,0,.18);overflow:hidden}
.s1{left:42px;top:108px}
.s2{left:614px;top:112px}
.s3{left:40px;top:473px}
.s4{left:610px;top:473px}
.s5{left:314px;top:816px}
.title{position:absolute;left:29px;top:10px;font-weight:700;font-size:35px;color:var(--navy);letter-spacing:.2px;white-space:nowrap}
.rule-top{position:absolute;left:28px;right:12px;top:59px;height:1px;background:var(--rule)}
.rule-bottom{position:absolute;left:28px;right:12px;top:275px;height:1px;background:var(--rule)}
.brand{position:absolute;font-weight:700;color:var(--navy);letter-spacing:-1px;white-space:nowrap;line-height:1}
.brand-top{right:14px;top:10px;font-size:38px}
.brand-bottom{right:32px;top:280px;font-size:25px}
.slide-no{position:absolute;right:24px;top:282px;font-weight:300;font-size:15px;color:var(--green)}
.lead{position:absolute;left:0;right:0;top:83px;text-align:center;font-size:13px;line-height:15.5px;color:var(--body)}
.portrait{position:absolute;top:147px;width:86px;height:86px;border-radius:50%;border:6px solid;background:radial-gradient(circle at 45% 40%,#7b6f66 0%,#3e3a38 70%)}
.p-red{left:90px;border-color:var(--red)}
.p-yellow{left:241px;border-color:var(--yellow)}
.p-green{left:393px;border-color:var(--green)}
.caption{position:absolute;top:242px;width:120px;text-align:center;font-weight:300;font-size:13px;color:var(--muted)}
.c1{left:73px}.c2{left:224px}.c3{left:376px}
.bullets{position:absolute;left:58px;top:94px;list-style:none;font-size:13px;line-height:18.5px;color:var(--body)}
.bullets li{position:relative;padding-left:13px}
.bullets li::before{content:"";position:absolute;left:0;top:7px;width:5px;height:5px;border-radius:50%;background:var(--red)}
.screen{position:absolute;left:261px;top:89px;width:236px;height:133px;border:1px solid #c9c9c9;box-shadow:0 1px 3px rgba(0,0,0,.2);background:linear-gradient(#eeeeee 0 12%,#0a7aa3 12% 72%,#f6f6f6 72%)}
.screen-note{position:absolute;left:316px;top:238px;width:120px;text-align:center;font-size:13px;color:var(--body)}
.divider{position:absolute;left:273px;top:67px;width:1px;height:200px;background:var(--rule)}
.venn{position:absolute;left:300px;top:70px;overflow:visible}
.venn text{font-family:"Open Sans",Arial,sans-serif;font-weight:700;font-size:13px;fill:#fff;text-anchor:middle}
.btn{position:absolute;top:178px;width:119px;height:44px;border-radius:13px;display:flex;align-items:center;justify-content:center;font-weight:700;font-size:13px}
.btn-yellow{left:54px;background:var(--yellow);color:#3d3d3d}
.btn-navy{left:216px;background:var(--navy);color:#fff}
.btn-red{left:377px;background:var(--red);color:#3d3d3d}
</style>
</head>
<body>

<section class="slide s1">
  <h1 class="title">First Topic Here</h1>
  <div class="brand brand-top">veltora</div>
  <div class="rule-top"></div>
  <p class="lead">Lorem ipsum dolor sit amet, consectetur adipiscing elit, sed do eiusmod<br>tempor incididunt ut labore et dolore magna aliqua. Ut enim ad minim<br>veniam, quis nostrud exercitation ullamco laboris nisi ut aliquip ex ea</p>
  <div class="portrait p-red" role="img" aria-label="Team member portrait photo"></div>
  <div class="portrait p-yellow" role="img" aria-label="Team member portrait photo"></div>
  <div class="portrait p-green" role="img" aria-label="Team member portrait photo"></div>
  <div class="caption c1">Photo Text</div>
  <div class="caption c2">Photo Text</div>
  <div class="caption c3">Photo Text</div>
  <div class="rule-bottom"></div>
  <div class="slide-no">Slide 01</div>
</section>

<section class="slide s2">
  <h1 class="title">First Topic Here</h1>
  <div class="brand brand-top">veltora</div>
  <div class="rule-top"></div>
  <ul class="bullets">
    <li>Sample bullet text</li><li>Another line</li><li>Next</li><li>Last text line</li>
    <li>Sample bullet text</li><li>Another line</li><li>Next</li><li>Last text line</li>
  </ul>
  <div class="screen" role="img" aria-label="Website screenshot of the Northpeak homepage"></div>
  <svg style="position:absolute;left:0;top:0" width="547" height="308" aria-hidden="true">
    <path d="M434 188 C472 198 468 252 438 252" fill="none" stroke="var(--red)" stroke-width="2.5" stroke-linecap="round"/>
    <path d="M442 184 L433 187 L439 195" fill="none" stroke="var(--red)" stroke-width="2.5" stroke-linecap="round" stroke-linejoin="round"/>
  </svg>
  <div class="screen-note">Screenshot here</div>
  <div class="rule-bottom"></div>
  <div class="slide-no">Slide 01</div>
</section>

<section class="slide s3">
  <h1 class="title">First Topic Here</h1>
  <div class="rule-top"></div>
  <p class="lead">Lorem ipsum dolor sit amet, consectetur adipiscing elit, sed do eiusmod<br>tempor incididunt ut labore et dolore magna aliqua. Ut enim ad minim<br>veniam, quis nostrud exercitation ullamco laboris nisi ut aliquip ex ea</p>
  <div class="portrait p-red" role="img" aria-label="Team member portrait photo"></div>
  <div class="portrait p-yellow" role="img" aria-label="Team member portrait photo"></div>
  <div class="portrait p-green" role="img" aria-label="Team member portrait photo"></div>
  <div class="caption c1">Photo Text</div>
  <div class="caption c2">Photo Text</div>
  <div class="caption c3">Photo Text</div>
  <div class="rule-bottom"></div>
  <div class="brand brand-bottom">veltora</div>
</section>

<section class="slide s4">
  <h1 class="title">First Topic Here</h1>
  <div class="brand brand-top">veltora</div>
  <div class="rule-top"></div>
  <ul class="bullets">
    <li>Sample bullet text</li><li>Another line</li><li>Next</li><li>Last text line</li>
    <li>Sample bullet text</li><li>Another line</li><li>Next</li><li>Last text line</li>
  </ul>
  <div class="divider"></div>
  <svg class="venn" width="240" height="190" viewBox="300 70 240 190" aria-label="Three-part overlap diagram">
    <g style="isolation:isolate">
      <circle cx="409" cy="133" r="52" fill="var(--red)"/>
      <circle cx="377" cy="193" r="52" fill="var(--navy)" style="mix-blend-mode:multiply"/>
      <circle cx="451" cy="193" r="52" fill="var(--yellow)" style="mix-blend-mode:multiply"/>
    </g>
    <text x="409" y="125">Sample</text>
    <text x="369" y="198">Sample</text>
    <text x="460" y="198">Sample</text>
  </svg>
  <div class="rule-bottom"></div>
  <div class="slide-no">Slide 01</div>
</section>

<section class="slide s5">
  <h1 class="title">First Topic Here</h1>
  <div class="rule-top"></div>
  <p class="lead">Lorem ipsum dolor sit amet, consectetur adipiscing elit, sed do eiusmod<br>tempor incididunt ut labore et dolore magna aliqua. Ut enim ad minim<br>veniam, quis nostrud exercitation ullamco laboris nisi ut aliquip ex ea</p>
  <div class="btn btn-yellow">Sample</div>
  <div class="btn btn-navy">Sample</div>
  <div class="btn btn-red">Sample</div>
  <div class="rule-bottom"></div>
  <div class="brand brand-bottom">veltora</div>
</section>

</body>
</html>
```